Plakat-Design für einen Pflegedienst
Zielgruppe
Unter Pflegedienst besteht jetzt seit 10 Jahren, Dazu würden wir gerne ein Werbeplakat an verschiedenen Standpunkten veröffentlichen. Draus sollte hervorgehen, dass wir 10 Jahre bestehen Bilder sollten aus den Portalen verwendet werden. Der Slogan könnte vielleicht lauten:
Seit 10 Jahren rund um die Uhr für Sie im Einsatz.
oder gerne auch eine andere Idee für den Slogan.
Die Plakate sollen bei 468 Aushang veröffentlicht werden. Da wir zwei Filialen betrieben, müssten zwei verschiedene Varianten mit zwei Logos und Telefonnummern erstellt werden.
Aufgabenstellung
Das Plakat sollte modern und elegant sein.

```html
<!DOCTYPE html>
<html lang="de">
<head>
<meta charset="UTF-8">
<title>Pflegedienst Plakat – Seit 10 Jahren</title>
<link rel="stylesheet" href="https://fonts.googleapis.com/css2?family=Bebas+Neue&family=Oswald:wght@300&family=Lato:wght@700;900&display=swap">
<style>
  :root {
    --yellow: #f2d04a;
    --yellow-light: #f4e07a;
    --yellow-deep: #efc43a;
    --teal: #35a0ab;
    --teal-text: #2b9aa6;
    --white: #ffffff;
    --box-white: #f7f7f5;
    --ink: #111111;
    --page: #ffffff;
  }
  * { box-sizing: border-box; margin: 0; padding: 0; }
  html, body {
    width: 1200px;
    height: 800px;
    overflow: hidden;
    background: var(--page);
  }
  .stage {
    position: relative;
    width: 1200px;
    height: 800px;
  }
  .poster {
    position: absolute;
    left: 332px;
    top: 20px;
    width: 796px;
    height: 1130px;
    transform: scale(0.6726);
    transform-origin: top left;
    background: var(--yellow);
    overflow: hidden;
  }
  .hero-photo {
    position: absolute;
    left: 0; top: 0;
    width: 796px;
    height: 590px;
    background:
      radial-gradient(ellipse at 30% 25%, var(--yellow-light) 0%, rgba(244,224,122,0) 60%),
      linear-gradient(180deg, var(--yellow) 0%, var(--yellow-deep) 100%);
  }
  .hero-photo::after {
    content: "";
    position: absolute;
    right: 0; top: 100px;
    width: 320px; height: 490px;
    background: linear-gradient(160deg, rgba(53,160,171,0) 0%, rgba(53,160,171,0.55) 55%, rgba(53,160,171,0.8) 100%);
  }
  .headline {
    position: absolute;
    left: 0;
    top: 264px;
    font-family: "Bebas Neue", "Oswald", sans-serif;
    color: var(--teal-text);
    list-style: none;
  }
  .headline-line {
    display: block;
    position: absolute;
    left: 0;
    height: 82px;
    padding-left: 12px;
    background: var(--box-white);
    font-size: 84px;
    line-height: 92px;
    letter-spacing: 1px;
    white-space: nowrap;
  }
  .headline-line--1 { top: 0;   width: 425px; }
  .headline-line--2 { top: 107px; width: 486px; }
  .headline-line--3 { top: 217px; width: 548px; padding-left: 20px; }
  .services {
    position: absolute;
    left: 0; top: 590px;
    width: 796px; height: 332px;
    background: var(--teal);
    color: var(--white);
  }
  .services-title {
    position: absolute;
    left: 27px; top: 32px;
    font-family: "Oswald", sans-serif;
    font-weight: 300;
    font-size: 44px;
    letter-spacing: 0.5px;
  }
  .services-list {
    position: absolute;
    left: 84px; top: 100px;
    list-style: none;
    font-family: "Lato", sans-serif;
    font-weight: 700;
    font-size: 26px;
  }
  .services-list li {
    height: 51px;
    display: flex;
    align-items: center;
  }
  .services-list li::before {
    content: "";
    width: 13px; height: 13px;
    border-radius: 50%;
    background: var(--white);
    margin-right: 12px;
  }
  .badge-24-7 {
    position: absolute;
    left: 558px; top: 74px;
    width: 190px; height: 190px;
  }
  .footer {
    position: absolute;
    left: 0; top: 922px;
    width: 796px; height: 208px;
    background: var(--yellow);
    font-family: "Lato", sans-serif;
    font-weight: 900;
    color: var(--teal-text);
    font-size: 29px;
    letter-spacing: 3px;
    line-height: 42px;
  }
  .footer-links {
    position: absolute;
    left: 25px; top: 45px;
  }
  .footer-brand {
    position: absolute;
    left: 364px; top: 82px;
    font-size: 44px;
    letter-spacing: 4px;
    color: var(--ink);
  }
  .footer-address {
    position: absolute;
    right: 30px; top: 40px;
    text-align: right;
    font-size: 31px;
    letter-spacing: 4px;
    line-height: 45px;
  }
</style>
</head>
<body>
<main class="stage">
  <article class="poster">
    <div class="hero-photo" role="img" aria-label="Foto einer Pflegekraft in türkisfarbener Kleidung mit Mundschutz, die in Superhelden-Pose die Faust nach oben streckt, vor gelbem Hintergrund"></div>

    <h1 class="headline">
      <span class="headline-line headline-line--1">Seit 10 Jahren</span>
      <span class="headline-line headline-line--2">Rund um die Uhr</span>
      <span class="headline-line headline-line--3">Für Sie im Einsatz</span>
    </h1>

    <section class="services">
      <h2 class="services-title">UNSERE LEISTUNGEN:</h2>
      <ul class="services-list">
        <li>...</li>
        <li>...</li>
        <li>...</li>
        <li>...</li>
      </ul>
      <svg class="badge-24-7" viewBox="0 0 180 180" aria-label="24/7 erreichbar">
        <g fill="none" stroke="#f2d04a" stroke-width="4" stroke-linecap="round">
          <path d="M164.3 124.7 A82 82 0 0 0 82.9 8.3"/>
          <path d="M22.8 43 A82 82 0 0 0 82.9 171.7"/>
        </g>
        <g fill="#f2d04a">
          <polygon points="70,8 87,-1 87,17"/>
          <polygon points="96,172 79,163 79,181"/>
        </g>
        <g transform="rotate(10 90 90)" fill="#f2d04a" font-family="Bebas Neue, Oswald, sans-serif">
          <text x="34" y="92" font-size="64">24</text>
          <text x="92" y="112" font-size="56">/</text>
          <text x="114" y="128" font-size="60">7</text>
        </g>
      </svg>
    </section>

    <footer class="footer">
      <div class="footer-links">
        <div>Website</div>
        <div>Social Media</div>
        <div>Telefonnummer</div>
      </div>
      <div class="footer-brand">LOGO</div>
      <address class="footer-address" style="font-style: normal;">
        <div>Kontakt</div>
        <div>Straße</div>
        <div>PLZ ORT</div>
      </address>
    </footer>
  </article>
</main>
</body>
</html>
```